Facial Cosmetic Business Card Design

I am a Physician certified in Lumivex injections, Sorelane fillers,& Chemical Peels.
I do no surgery
I have 20 years experience in facial cosmetics
30+ years medical experience
name is not TM but thought something like "Radiant Visage" catches what I do and the look I get with minimal to no downtime and no recovery time.
I do home parties and also private home consultations and treatments in a relaxed atmosphere with no pressure.
Aestheology services upon referral to a private associate as well.
I have no logo, photo's or desigs so I am ope to suggestions

To all the MD is my medical degree

the MNGGC are my board certifications stands for Member National Guild General Care
4816 Cedar Hollow Lane is my office home address
4045518832 is my cell/office number or contact info

Thanks

Reason: Sorry was out of town I like a few of the designs so I have enough to choose from set tweeks to be done with prof degree and address mixup. Once i see corrections I will choose approp one thanks all Dr Kessler

Target Market(s)

mostly wome do these procedures usually i the above 35 crowd certainly over 40 crowd for sure

Industry/Entity Type

Medical

Contact Information for Business Card

Radiant Visage, Daniel Kessler MD, MNGGC
4816 Cedar Hollow Lane
Willowmere, Ga. 30999
O:404-551-9016
C:404-551-8832
F:404-551-9070

```html
<!DOCTYPE html>
<html lang="en">
<head>
<meta charset="utf-8">
<title>Radiant Visage – Business Card</title>
<link rel="stylesheet" href="https://fonts.googleapis.com/css2?family=Arimo:wght@400;700&display=swap">
<style>
  :root {
    --backdrop: #d9d4ce;
    --card-black: #0a0a0a;
    --accent-red: #c8262d;
    --text-white: #f4f4f4;
    --text-grey: #c9c9c9;
  }
  html, body {
    margin: 0;
    width: 1200px;
    height: 723px;
    overflow: hidden;
    background: var(--backdrop);
    font-family: "Arimo", Arial, sans-serif;
  }
  .canvas {
    position: relative;
    width: 1200px;
    height: 723px;
    display: flex;
    align-items: center;
    justify-content: center;
  }
  .card {
    position: relative;
    width: 380px;
    height: 664px;
    background: var(--card-black);
    overflow: hidden;
    box-shadow: 0 10px 30px rgba(0,0,0,.35);
  }
  .card__art {
    position: absolute;
    inset: 0;
    background:
      radial-gradient(ellipse 70% 40% at 55% 62%, rgba(90,90,90,.28), transparent 70%),
      radial-gradient(ellipse 60% 30% at 40% 30%, rgba(80,80,80,.22), transparent 70%);
  }
  .card__content {
    position: relative;
    padding: 44px 30px 0 36px;
    color: var(--text-white);
  }
  .brand {
    display: flex;
    align-items: center;
    justify-content: flex-end;
    gap: 10px;
    margin-bottom: 50px;
  }
  .brand__dot {
    width: 14px;
    height: 14px;
    border-radius: 50%;
    background: var(--accent-red);
  }
  .brand__name {
    color: var(--accent-red);
    font-size: 26px;
    font-weight: 400;
  }
  .person__name {
    font-size: 25px;
    font-weight: 700;
    margin: 0;
    letter-spacing: .2px;
  }
  .person__credential {
    color: var(--text-grey);
    font-size: 19px;
    margin: 6px 0 30px 120px;
  }
  .address {
    font-style: normal;
    font-size: 21px;
    line-height: 1.3;
    color: var(--text-white);
    margin-bottom: 34px;
  }
  .contacts {
    list-style: none;
    margin: 0;
    padding: 0;
  }
  .contact {
    margin-bottom: 26px;
    font-size: 25px;
    line-height: 1.1;
    color: var(--text-white);
  }
  .contact__icon {
    display: block;
    width: 28px;
    height: 28px;
    margin: 0 0 4px 160px;
    fill: var(--accent-red);
  }
</style>
</head>
<body>
<main class="canvas">
  <article class="card">
    <div class="card__art" role="img" aria-label="Faint grey line illustration of a woman's profile with flowing hair"></div>
    <div class="card__content">
      <header class="brand">
        <span class="brand__dot"></span>
        <span class="brand__name">Radiant Visage</span>
      </header>
      <h1 class="person__name">Daniel Kessler MD,</h1>
      <p class="person__credential">MNGGC</p>
      <address class="address">4816 Cedar Hollow Lane<br>Willowmere, Ga. 30999</address>
      <ul class="contacts">
        <li class="contact">
          <svg class="contact__icon" viewBox="0 0 24 24" aria-label="Office phone"><path d="M6.6 10.8a15.1 15.1 0 0 0 6.6 6.6l2.2-2.2c.3-.3.7-.4 1-.2 1.1.4 2.3.6 3.6.6.6 0 1 .4 1 1V20c0 .6-.4 1-1 1A17 17 0 0 1 3 4c0-.6.4-1 1-1h3.5c.6 0 1 .4 1 1 0 1.3.2 2.5.6 3.6.1.3 0 .7-.2 1z"/></svg>
          404-551-9016
        </li>
        <li class="contact">
          <svg class="contact__icon" viewBox="0 0 24 24" aria-label="Cell phone"><path d="M7 1h10a2 2 0 0 1 2 2v18a2 2 0 0 1-2 2H7a2 2 0 0 1-2-2V3a2 2 0 0 1 2-2zm0 3v14h10V4zm5 15.2a1 1 0 1 0 0 2 1 1 0 0 0 0-2z"/></svg>
          404-551-8832
        </li>
        <li class="contact">
          <svg class="contact__icon" viewBox="0 0 24 24" aria-label="Fax"><path d="M6 2h9l3 3v5H6zM2 11h20v10H2zm3 3v2h4v-2zm0 3v2h4v-2zm7-3v2h2v-2zm3 0v2h2v-2zm-3 3v2h2v-2zm3 0v2h2v-2z"/></svg>
          404-551-9070
        </li>
      </ul>
    </div>
  </article>
</main>
</body>
</html>
```